Innovative Consulting Firm Needs New Business Cards and Stationary

Our Innovative Consulting Firm, Larkfield Consulting, is in need of new business cards and stationary designs. We want two-sided cards that incorporate our logo, which is attached. We are looking for something not too formal, but is professional and slick.

Card should have the following information:
Name (ex. Tom Bradley)
Title (ex. Manager)
Address (ex. 24680 Cedar Lane)
Address 2 (ex. Suite 100)
City
State
Zip Code
Mobile
Email

The card should also have our website: www.larkfieldconsulting.example

Industry/Entity Type

Management Consulting

Contact Information for Business Card

Name (ex. Tom Bradley)
Title (ex. Manager)
Address 2 (ex. Suite 100)
City
State
Zip Code
Mobile
Email

Font styles to use
Sans Serif

Requirements
Must have
• The colors on the card must match the colors in the logo. The exact color codes are attached in a pdf.
Nice to have
• The Company's Tagline is "Focused on your Future". This might be nice to incorporate, but not necessary.

```html
<!DOCTYPE html>
<html lang="en">
<head>
<meta charset="utf-8">
<title>Larkfield Consulting – Business Card</title>
<link href="https://fonts.googleapis.com/css2?family=Source+Sans+3:wght@400;600;700&display=swap" rel="stylesheet">
<style>
  :root {
    --backdrop: #cdb89c;
    --card: #f6f3ec;
    --navy: #1f4e79;
    --gold: #e9a813;
    --gold-soft: #f3dfae;
    --shadow: rgba(70, 50, 25, 0.22);
  }
  * { box-sizing: border-box; margin: 0; padding: 0; }
  html, body {
    width: 1200px; height: 823px; overflow: hidden;
    background: var(--backdrop);
    font-family: "Source Sans 3", "Myriad Pro", sans-serif;
    color: var(--navy);
  }
  .sheet {
    width: 1200px; height: 823px;
    display: flex; align-items: center; justify-content: center; gap: 60px;
  }
  .card {
    position: relative;
    width: 520px; height: 297px;
    background: var(--card);
    box-shadow: 0 10px 28px var(--shadow);
    overflow: hidden;
  }

  /* Contact side */
  .ornament-area {
    position: absolute; left: 0; top: 126px;
    width: 480px; height: 12px;
    background: linear-gradient(90deg, var(--gold), var(--gold-soft));
  }
  .contact-person {
    position: absolute; left: 232px; top: 46px;
    line-height: 1.15;
  }
  .person-icon { position: absolute; left: -30px; top: 20px; }
  .person-name { font-size: 22px; font-weight: 700; }
  .person-title { font-size: 17px; }
  .person-phone { font-size: 19px; font-weight: 600; margin-top: 4px; letter-spacing: 0.5px; }
  .contact-address {
    position: absolute; left: 120px; top: 166px;
    font-size: 19px; line-height: 1.15; font-style: normal;
  }
  .contact-address .sep { color: var(--navy); }

  /* Brand side */
  .card--brand {
    display: flex; flex-direction: column; align-items: center; justify-content: center;
    padding: 0 24px;
  }
  .brand-name {
    display: flex; align-items: center; gap: 12px;
    font-size: 46px; font-weight: 600; letter-spacing: 0.5px;
    line-height: 1; white-space: nowrap;
  }
  .brand-dot { width: 15px; height: 15px; border-radius: 50%; background: var(--gold); flex: none; }
  .brand-links {
    margin-top: 34px;
    display: flex; align-items: center; gap: 12px;
    font-size: 15px; white-space: nowrap;
  }
  .divider { width: 2px; height: 20px; background: var(--gold); }
</style>
</head>
<body>
<main class="sheet">

  <section class="card card--contact" aria-label="Card back with contact details">
    <div class="ornament-area" role="img" aria-label="Brand ornament area"></div>
    <div class="contact-person">
      <svg class="person-icon" width="18" height="18" viewBox="0 0 18 18" aria-hidden="true">
        <circle cx="9" cy="5" r="4" fill="var(--gold)"/>
        <path d="M1 18 C1 11, 17 11, 17 18 Z" fill="var(--gold)"/>
      </svg>
      <p class="person-name">Tom Bradley</p>
      <p class="person-title">Manager</p>
      <p class="person-phone">(0155) 555 010 234</p>
    </div>
    <address class="contact-address">
      <p>ex. 24680 Cedar Lane</p>
      <p>ex. Suite 100</p>
      <p>City <span class="sep">|</span> State <span class="sep">|</span> Zip Code</p>
    </address>
  </section>

  <section class="card card--brand" aria-label="Card front with company name">
    <h1 class="brand-name"><span class="brand-dot"></span>Larkfield Consulting</h1>
    <p class="brand-links">
      <span>www.larkfieldconsulting.example</span>
      <span class="divider"></span>
      <span>info@larkfieldconsulting.example</span>
    </p>
  </section>

</main>
</body>
</html>
```